IT consultancy business needs logo and business card designed

I need designed business card. it needs to have some wow effect, but simple, corporate and business focused. We provide corporate grade IT services to medium size businesses. These services are IT support over phone, email, in person, VOIP services, IT security , networking - everything that helps business be productivy.

Out tag line will be something along these lines" promoting business growth through use of technology:.

I need a logo designed as well. I am happy to use any colors/theme, perhaps neutral colours, earthy?

Priority: NICE looking, wow design, nice fonts, colors etc... nice logo, business focused but HAS to be modern, wow effect. I will accept anything that looks really cool.

Target Market(s)

Target market are businesses with 20-100 employees. Audience are business decision makers, like general managers, CEO, directors, those are the one seeing this business card;

Industry/Entity Type

Business

Contact Information for Business Card

I am totally flexible, suprise me me something creative:

Dorian Velmek logo on this side(you will design)
managing director ------------------------------- this is line
slogan: technology.delivered.simple

Level 3, 48 Pemberwick Street, Sydney, NSW 2000
dorian@tovrani.com.au
www.tovrani.com.au

back page: logo and slogan: promoting business growth through use of technolog

Requirements
Must have
• Must look modern, cool., wow effect, yet simple and professional.

```html
<!DOCTYPE html>
<html lang="en">
<head>
<meta charset="utf-8">
<title>Dorian Velmek – Business Card</title>
<link rel="stylesheet" href="https://fonts.googleapis.com/css2?family=Arimo:wght@400&family=Pacifico&display=swap">
<style>
  :root {
    --page: #ffffff;
    --card: #ffffff;
    --card-edge: #cfcfcf;
    --card-shadow: #c9c9c9;
    --brand-blue: #1f4fc0;
    --name-sky: #5ec3dd;
    --title-blue: #4a8fd8;
    --tagline-blue: #2a5fb0;
    --ink: #222222;
  }
  html, body {
    margin: 0;
    padding: 0;
    width: 1200px;
    height: 675px;
    overflow: hidden;
    background: var(--page);
  }
  .business-card {
    position: absolute;
    left: 38px;
    top: 18px;
    width: 1125px;
    height: 641px;
    box-sizing: border-box;
    background: var(--card);
    border: 1px solid var(--card-edge);
    box-shadow: 5px 5px 0 var(--card-shadow);
    font-family: "Arimo", Arial, sans-serif;
    text-align: center;
  }
  .brand-mark {
    position: absolute;
    left: 0;
    right: 0;
    top: 140px;
    display: flex;
    justify-content: center;
    align-items: center;
    gap: 18px;
  }
  .brand-dot {
    width: 60px;
    height: 60px;
    border-radius: 50%;
    background: var(--brand-blue);
  }
  .brand-name {
    font-size: 52px;
    color: var(--brand-blue);
    line-height: 1;
  }
  .holder-name {
    position: absolute;
    left: 0;
    right: 0;
    top: 290px;
    margin: 0;
    font-family: "Pacifico", cursive;
    font-weight: 400;
    font-size: 64px;
    line-height: 1.1;
    color: var(--name-sky);
  }
  .holder-title {
    position: absolute;
    left: 0;
    right: 0;
    top: 372px;
    margin: 0;
    font-size: 40px;
    line-height: 1;
    color: var(--title-blue);
  }
  .tagline {
    position: absolute;
    left: 0;
    right: 0;
    top: 422px;
    margin: 0;
    font-size: 31.5px;
    line-height: 1;
    color: var(--tagline-blue);
  }
  .contact-line {
    position: absolute;
    left: 0;
    right: 0;
    margin: 0;
    font-size: 30px;
    line-height: 1;
    color: var(--ink);
  }
  .contact-phone { top: 467px; }
  .contact-email { top: 515px; }
</style>
</head>
<body>
  <main class="business-card">
    <div class="brand-mark">
      <span class="brand-dot" aria-hidden="true"></span>
      <span class="brand-name">Tovrani</span>
    </div>
    <h1 class="holder-name">Dorian Velmek</h1>
    <p class="holder-title">Managing Director</p>
    <p class="tagline">Promoting Business Growth Through Use Of Technology:</p>
    <p class="contact-line contact-phone">(02) 5550 1847</p>
    <p class="contact-line contact-email">dorian@tovrani.com.au</p>
  </main>
</body>
</html>
```